Heritage Hollow Business Cards

Require a business card design. <br/><br/>Needs to include logo (either round or long version) plus these details:<br/>Maya Torvel<br/>Heritage Hollow<br/>maya@quonbrook.com.au<br/>02 6481 7390<br/>PO Box Glenwarra NSW 2913<br/>www.heritagehollow.com.au<br/><br/>I need in an editable format so that I can create for multiple staff members. <br/><br/>

Target Market(s)

We are an online store selling renovation products to home owners are builders. Looking for a classic classy design.

Industry/Entity Type

Home And Garden

Contact Information for Business Card

Maya Torvel
Heritage Hollow
maya@quonbrook.com.au
02 6481 7390
PO Box Glenwarra NSW 2913
www.heritagehollow.com.au

Colors

Designer to choose colors to be used in the design.

Requirements
Must have
• Must include Logo.

```html
<!DOCTYPE html>
<html lang="en">
<head>
<meta charset="utf-8">
<title>Heritage Hollow Business Cards</title>
<link href="https://fonts.googleapis.com/css2?family=Arimo:wght@400;700&display=swap" rel="stylesheet">
<style>
  :root {
    --backdrop: #d6d6d6;
    --card-light: #ffffff;
    --card-dark: #231f20;
    --ink: #1a1a1a;
    --ink-soft: #2b2b2b;
    --rule: #c8c8c8;
    --mark-light: #e6e6e6;
  }
  * { margin: 0; padding: 0; box-sizing: border-box; }
  html, body {
    width: 1200px; height: 802px; overflow: hidden;
    background: var(--backdrop);
    font-family: "Arimo", Arial, sans-serif;
  }
  .stage { position: relative; width: 1200px; height: 802px; }
  .card {
    position: absolute; top: 274px;
    width: 442px; height: 263px;
  }
  .card--front { left: 136px; background: var(--card-light); color: var(--ink); }
  .card--back { left: 624px; background: var(--card-dark); }

  .brand {
    position: absolute; display: flex; align-items: center; gap: 10px;
    font-weight: 400; font-size: 30px; letter-spacing: 0.2px; white-space: nowrap;
  }
  .brand__dot { width: 26px; height: 26px; border-radius: 50%; border: 2px solid currentColor; }
  .card--front .brand { left: 154px; top: 80px; color: var(--ink); }
  .card--back .brand { left: 95px; top: 148px; color: var(--mark-light); }

  .holder {
    position: absolute; left: 27px; top: 157px; width: 386px;
    display: flex; align-items: center; gap: 12px;
  }
  .holder__name { font-weight: 700; font-size: 15px; letter-spacing: 0.6px; white-space: nowrap; }
  .holder__rule { flex: 1; height: 1px; background: var(--rule); }

  .contact { position: absolute; left: 27px; top: 194px; list-style: none; }
  .contact li {
    display: flex; align-items: center; gap: 3px;
    font-size: 12.5px; line-height: 17px; color: var(--ink-soft);
  }
  .contact svg { width: 13px; height: 13px; flex: none; }

  .office {
    position: absolute; right: 31px; top: 197px; text-align: right;
    font-size: 12.5px; line-height: 16.5px; color: var(--ink-soft);
  }
  .office__company { font-weight: 700; letter-spacing: 0.3px; color: var(--ink); }

  .card__band { position: absolute; left: 0; bottom: 0; width: 100%; height: 8px; background: var(--card-dark); }
</style>
</head>
<body>
<main class="stage">
  <section class="card card--front" aria-label="Business card front">
    <div class="brand"><span class="brand__dot"></span><span>Heritage Hollow</span></div>

    <div class="holder">
      <span class="holder__name">MAYA TORVEL</span>
      <span class="holder__rule"></span>
    </div>

    <ul class="contact">
      <li>
        <svg viewBox="0 0 16 16" aria-hidden="true"><rect x="1" y="1" width="14" height="14" rx="3" fill="none" stroke="#1a1a1a" stroke-width="1.4"/><path d="M5 4.2c.6-.5 1.2-.3 1.5.3l.6 1.2c.2.4 0 .8-.3 1l-.5.4c.4 1 1.3 1.9 2.3 2.4l.4-.5c.3-.3.7-.4 1-.2l1.2.6c.6.3.7 1 .2 1.5-.8.8-2 .9-3.2.2C6.4 10.3 5 8.7 4.6 7.2 4.3 6 4.4 4.8 5 4.2z" fill="#1a1a1a"/></svg>
        <span>02 6481 7390</span>
      </li>
      <li>
        <svg viewBox="0 0 16 16" aria-hidden="true"><rect x="1" y="3" width="14" height="10" fill="#1a1a1a"/><path d="M1.5 3.5L8 9l6.5-5.5" fill="none" stroke="#fff" stroke-width="1.2"/></svg>
        <span>maya@quonbrook.com.au</span>
      </li>
      <li>
        <svg viewBox="0 0 16 16" aria-hidden="true"><circle cx="8" cy="8" r="7" fill="#1a1a1a"/><g fill="none" stroke="#fff" stroke-width="0.9"><ellipse cx="8" cy="8" rx="3" ry="7"/><path d="M1 8h14M2 4.5h12M2 11.5h12"/></g></svg>
        <span>www.heritagehollow.com.au</span>
      </li>
    </ul>

    <address class="office" style="font-style:normal">
      <div class="office__company">HERITAGE HOLLOW</div>
      <div>PO Box Glenwarra</div>
      <div>NSW 2913</div>
    </address>

    <div class="card__band"></div>
  </section>

  <section class="card card--back" aria-label="Business card back">
    <div class="brand"><span class="brand__dot"></span><span>Heritage Hollow</span></div>
  </section>
</main>
</body>
</html>
```